Book cover for book of Poems "Lanternfall"

I have written a book of poems. The book is titled "Lanternfall" and has 160 pages. The poems were written mostly during my youth but there are newer poems also written over the past 10 years (I'm 42 now). They are mostly about love, loss, social conformity, and nature. I'm influenced a lot by the English Romantic Poets, gothic motives, and 80s music by bands such as The Vell, Porvana & the Quillets, and Tabberley. I need an original book cover design for my book. Attached are samples of designs I like and few of my poems. The cover will be a hardcover and I need design for Front Cover, Back Cover, and Spine. Dimension is 6"x9". Front Cover should have name of book "Lanternfall" and name of author "Ravi Dunsker". Thanks.
Updates

Further details which I should have included in my original brief -The book cover will be a hard cover. Design is required for front cover, back cover, and spine. Dimension is 6x9.Front should have book title "Lanternfall" and author's name "Ravi Dunsker". Added Monday, December 19, 2016

Target Market(s)

Mostly friends and family

Requirements
Must have
• I don't mind a design where lanternfall is spelled out in big capital letters and text from one of my poems is inside, like the sample I've attached.

```html
<!DOCTYPE html>
<html lang="en">
<head>
<meta charset="utf-8">
<title>Lanternfall — Ravi Dunsker — Book Cover</title>
<link href="https://fonts.googleapis.com/css2?family=League+Gothic&family=Oswald:wght@400;500&family=Pathway+Gothic+One&display=swap" rel="stylesheet">
<style>
  :root {
    --ink: #000000;
    --yellow: #fff200;
    --grey-text: #5b5656;
    --grid-text: #3d3b3b;
    --white: #ffffff;
  }
  * { margin: 0; padding: 0; box-sizing: border-box; }
  html, body { width: 1200px; height: 843px; overflow: hidden; background: var(--ink); }

  .cover-wrap { position: relative; width: 1200px; height: 843px; background: var(--ink); }

  /* Back cover */
  .back-cover { position: absolute; left: 0; top: 0; width: 564px; height: 843px; }
  .intro { position: absolute; left: 38px; top: 110px; font-family: "League Gothic", sans-serif;
           font-size: 28px; line-height: 30.2px; color: var(--grey-text); text-transform: uppercase; }
  .intro .line { display: block; white-space: nowrap; }
  .intro .line--bright { color: var(--white); }
  .intro .line--title { font-family: "Oswald", sans-serif; font-weight: 400; color: var(--yellow);
                        font-size: 36px; line-height: 48px; letter-spacing: 22px; margin: -4px 0 -6px; }

  /* Spine */
  .spine { position: absolute; left: 564px; top: 0; width: 74px; height: 843px; background: var(--yellow); }
  .spine-title { position: absolute; left: 4px; top: 32px; writing-mode: vertical-rl; white-space: nowrap;
                 font-family: "Oswald", sans-serif; font-weight: 500; font-size: 50px; line-height: 64px;
                 letter-spacing: 32px; color: var(--ink); }
  .spine-author { position: absolute; left: 22px; top: 668px; writing-mode: vertical-rl; white-space: nowrap;
                  font-family: "Oswald", sans-serif; font-weight: 400; font-size: 16px; line-height: 24px;
                  letter-spacing: 7px; color: var(--ink); }

  /* Front cover */
  .front-cover { position: absolute; left: 638px; top: 0; width: 562px; height: 843px; }
  .title-grid { position: absolute; left: 38px; top: 32px; width: 489px;
                font-family: "Pathway Gothic One", sans-serif; font-size: 21px; color: var(--grid-text);
                text-transform: uppercase; }
  .title-grid .row { display: flex; justify-content: space-between; height: 23.1px; line-height: 23.1px;
                     white-space: nowrap; }
  .title-grid .hl { color: var(--yellow); font-weight: normal; }
  .front-author { position: absolute; left: 37px; top: 786px; width: 492px; display: flex;
                  justify-content: space-between; font-family: "Oswald", sans-serif; font-weight: 400;
                  font-size: 19px; color: var(--white); }
  .front-author .gap { width: 60px; }
</style>
</head>
<body>
<div class="cover-wrap">

  <section class="back-cover">
    <p class="intro">
      <span class="line">Hi.</span>
      <span class="line line--bright">I am Ravi Dunsker.</span>
      <span class="line">You are holding a book of my momoirs.</span>
      <span class="line">They are in the form of poems.</span>
      <span class="line">I call it</span>
      <span class="line line--title">Lanternfall</span>
      <span class="line">The poems were written</span>
      <span class="line">mostly during my youth.</span>
      <span class="line">There are newer poems also written</span>
      <span class="line">over the past 10 years (I'm 42 now).</span>
      <span class="line">They are mostly about:</span>
      <span class="line">Love.</span>
      <span class="line">Loss.</span>
      <span class="line">Social conformity.</span>
      <span class="line">And nature.</span>
      <span class="line">I'm influenced a lot by</span>
      <span class="line">the English Romantic poets.</span>
      <span class="line">Gothic motives.</span>
      <span class="line">80s music by bands such as</span>
      <span class="line">The Vell.</span>
      <span class="line">Porvana &amp; the Quillets.</span>
      <span class="line">And Tabberley.</span>
      <span class="line line--bright">Please enjoy.</span>
    </p>
  </section>

  <section class="spine">
    <div class="spine-title">LANTERNFALL</div>
    <div class="spine-author">RAVI DUNSKER</div>
  </section>

  <section class="front-cover">
    <div class="title-grid" aria-label="Lanternfall, spelled within a list of poem titles">
      <div class="row"><span>Ember</span><span>Hol<b class="hl">l</b>ow</span><span>Whispers at dusk</span><span>Ash tree</span><span>The kept, the keeper</span></div>
      <div class="row"><span>Half-lit hours</span><span>Again…</span><span>Hymn to rain</span><span>Night song</span></div>
      <div class="row"><span>The fog, the moor</span><span>How</span><span>Song of bells</span><span>On grief</span><span>Stay</span><span>To the comets</span></div>
      <div class="row"><span>Old town</span><span>Wandering</span><span>For my brothers</span><span>Midnight</span><span>Wh<b class="hl">a</b>t the tide knew</span></div>
      <div class="row"><span>Stones weep</span><span>Echoes and silence</span><span>Pilgrim</span><span>Undertow</span></div>
      <div class="row"><span>Tonight I walk the shore alone</span><span>Longing</span><span>Visions</span><span>Hold me</span></div>
      <div class="row"><span>Have you seen</span><span>Farewell</span><span>The lighthouse</span><span>Never turn back</span></div>
      <div class="row"><span>Do not follow i<b class="hl">n</b> the rain my love</span><span>Always</span><span>Old letters</span></div>
      <div class="row"><span>A quiet girl</span><span>That silent thief</span><span>In bone and ash</span><span>My absent friend</span></div>
      <div class="row"><span>Remembering her</span><span>Her hands</span><span>Tender ruin</span><span>So radiant</span></div>
      <div class="row"><span>Do you know how bright you shine</span><span>Las<b class="hl">t</b> winter</span><span>Kings and saints</span></div>
      <div class="row"><span>To a lost one</span><span>To stillness</span><span>Fear</span><span>Beneath a pine</span><span>Past</span></div>
      <div class="row"><span>So near, y<b class="hl">e</b>t so gone</span><span>Faith</span><span>A meadow</span><span>Hush</span><span>Drifting sparks</span></div>
      <div class="row"><span>7 winters</span><span>Ivy</span><span>A sailor's lament</span><span>Hoping for unlikely endings</span></div>
      <div class="row"><span>That night</span><span>The shade of grief</span><span>The storms I have weathered</span></div>
      <div class="row"><span>A haunted hall</span><span>This crumbling chapel</span><span>My fi<b class="hl">r</b>st winter snow</span></div>
      <div class="row"><span>To my sister and brother</span><span>The vigil</span><span>Alone</span><span>Draw you</span><span>The pilgrim</span></div>
      <div class="row"><span>Fall into my heart</span><span>I have a dream older than dreams</span><span>My days are a verse</span></div>
      <div class="row"><span>Betrayal</span><span>Do <b class="hl">n</b>ot look back</span><span>Tonight I sang for you</span><span>The leaving</span></div>
      <div class="row"><span>A tune softer than rain</span><span>The raven's hymn</span><span>I weep for Elena</span></div>
      <div class="row"><span>The wide grey</span><span>Desire</span><span>Grief is grey</span><span>Lament</span><span><b class="hl">F</b>ar off, so near</span></div>
      <div class="row"><span>That smile on your lips</span><span>I'm falling down</span><span>Touch</span><span>I want you</span><span>The owl</span></div>
      <div class="row"><span>Shadows unchained</span><span>Madness rising</span><span>Ruins of longing</span></div>
      <div class="row"><span>The pale one</span><span>The vow</span><span>I s<b class="hl">a</b>y goodbye</span><span>Carry me</span><span>My guiding moon</span></div>
      <div class="row"><span>Comma comma</span><span>Cold ash</span><span>Edge of night</span><span>Pulse</span><span>Souls like ours</span></div>
      <div class="row"><span>Then and now</span><span>I lost my voice</span><span>I long to die a death in verse</span></div>
      <div class="row"><span>I wish I could learn to fly</span><span><b class="hl">L</b>ight with meaning</span><span>Fate or chance</span></div>
      <div class="row"><span>The first &amp; last</span><span>He</span><span>Those were the nights</span><span>Starborn</span></div>
      <div class="row"><span>The falling comets</span><span>The kindest soul I know</span><span>The quiet hour</span></div>
      <div class="row"><span>Us and them</span><span>There's a stillness in your voice</span><span>Say I'm <b class="hl">l</b>ost</span></div>
      <div class="row"><span>This dusk</span><span>We've become the tide and shore</span><span>We were…</span></div>
      <div class="row"><span>Won't</span><span>Let</span><span>Us</span><span>Fall</span><span>Dreamer</span><span>But</span><span>You</span></div>
    </div>

    <div class="front-author" aria-label="Ravi Dunsker">
      <span>R</span><span>A</span><span>V</span><span>I</span><span class="gap"></span><span>D</span><span>U</span><span>N</span><span>S</span><span>K</span><span>E</span><span>R</span>
    </div>
  </section>

</div>
</body>
</html>
```